hair salon business Card Design

My business name is Hair & Beauty @ Corrabin I want a Hot Pink and black business card with a loyalty program on the back after every 2nd haircut the third has $5 off and I will whole punch the squares My business phone number is (07) 54 913 668 address is Shop 2 3/9 Wollard st Corrabin Qld 4571 find us on Friendbook should be on the card somewhere with the Friendbook logo also a space alocated for your next appointment date n time also would like your har stylists name is Tess on the card somewhere easy to read you can check out my Friendbook site for images of my logo n shop signage

Industry/Entity Type

Hair

```html
<!DOCTYPE html>
<html lang="en">
<head>
<meta charset="utf-8">
<title>Hair &amp; Beauty @ Corrabin – Business Cards</title>
<link rel="stylesheet" href="https://fonts.googleapis.com/css2?family=Quicksand:wght@500;700&family=Courgette&family=Open+Sans:ital,wght@1,800&display=swap">
<style>
  :root {
    --pink: #d0148f;
    --pink-deep: #a80c72;
    --pink-soft: #f6d3ea;
    --ink: #262626;
    --ink-deep: #1a1a1a;
    --grey: #4a4a4a;
    --white: #ffffff;
    --stage: #e9e5e0;
  }
  * { box-sizing: border-box; margin: 0; padding: 0; }
  html, body { width: 1200px; height: 729px; overflow: hidden; }
  body {
    background: var(--stage);
    position: relative;
    font-family: "Quicksand", sans-serif;
    color: var(--white);
  }
  .card {
    position: absolute;
    width: 560px;
    height: 350px;
    overflow: hidden;
    box-shadow: 0 6px 18px rgba(0,0,0,.25);
  }

  /* ---------- loyalty / appointment side ---------- */
  .card--loyalty { left: 50px; top: 40px; background: var(--ink); }
  .card--loyalty .flourish {
    position: absolute; left: 0; top: 0; width: 300px; height: 272px;
    background: radial-gradient(ellipse at 45% 40%, rgba(255,255,255,.10), rgba(255,255,255,0) 70%);
  }
  .stylist { position: absolute; left: 38px; top: 60px; }
  .stylist__lead { font-weight: 700; font-size: 22px; line-height: 1; }
  .stylist__name { font-family: "Courgette", cursive; font-size: 28px; color: var(--pink); line-height: 1.2; }

  .punch { position: absolute; left: 350px; top: 26px; display: flex; gap: 10px; }
  .punch__slot { display: flex; align-items: flex-end; }
  .punch__box { width: 22px; height: 22px; background: #cfcfcf; border-radius: 3px; }
  .punch__num { font-weight: 700; font-size: 30px; line-height: .8; color: #6a6a6a; margin-left: -4px; }
  .offer { position: absolute; left: 346px; top: 72px; font-weight: 700; font-size: 15px; line-height: 1.25; }
  .offer em { font-style: normal; color: var(--pink); }

  .appointment { position: absolute; left: 245px; top: 128px; width: 292px; border-radius: 6px; overflow: hidden; }
  .appointment__head {
    background: var(--pink); height: 26px; padding-left: 36px;
    font-weight: 700; font-size: 17px; line-height: 26px;
  }
  .appointment__row { display: flex; height: 40px; }
  .appointment__icon { width: 26px; background: #8c8c8c; display: flex; align-items: center; justify-content: center; }
  .appointment__cell { flex: 1; background: var(--white); border-left: 1px solid var(--pink-soft); }
  .appointment__row--time .appointment__cell {
    background: var(--pink-soft); color: var(--pink);
    font-weight: 700; font-size: 11px; line-height: 1.05;
    text-align: right; padding: 6px 8px 0 0;
  }

  .band { position: absolute; left: 0; bottom: 0; width: 100%; height: 78px; background: var(--pink); }
  .band__name { position: absolute; left: 36px; top: 10px; font-weight: 700; text-align: center; }
  .band__name b { display: block; font-size: 28px; line-height: 1.05; }
  .band__name span { display: block; font-size: 19px; font-weight: 700; }
  .band__rule { position: absolute; left: 240px; top: 10px; width: 1px; height: 58px; background: rgba(255,255,255,.7); }
  .social { position: absolute; left: 254px; top: 10px; }
  .social__lead { font-family: "Courgette", cursive; font-size: 19px; }
  .social__page { display: flex; align-items: center; gap: 6px; font-weight: 700; font-size: 14px; margin-top: 2px; }
  .social__mark { width: 13px; height: 13px; background: var(--white); }

  /* ---------- contact side ---------- */
  .card--contact {
    left: 590px; top: 339px;
    background: linear-gradient(180deg, var(--pink) 0%, var(--pink-deep) 68%);
  }
  .card--contact .flourish {
    position: absolute; left: 250px; top: 0; width: 310px; height: 240px;
    background: radial-gradient(ellipse at 60% 30%, rgba(255,255,255,.16), rgba(255,255,255,0) 70%);
  }
  .brand { position: absolute; left: 0; top: 88px; width: 100%; text-align: center; font-weight: 700; }
  .brand b { display: block; font-size: 46px; line-height: 1.05; }
  .brand span { display: block; font-size: 30px; }
  .contact-band { position: absolute; left: 0; bottom: 0; width: 100%; height: 112px; background: var(--grey); }
  .contact-band__pill {
    position: absolute; left: 26px; top: -8px; width: 30px; height: 96px;
    background: var(--white); border-radius: 15px;
    display: flex; flex-direction: column; align-items: center; gap: 10px; padding-top: 14px;
  }
  .contact-band__icon { width: 22px; height: 22px; border-radius: 50%; background: var(--pink); display: flex; align-items: center; justify-content: center; }
  .contact-band__lines {
    position: absolute; left: 74px; top: 8px;
    font-family: "Open Sans", sans-serif; font-style: italic; font-weight: 800;
    font-size: 18px; line-height: 34px;
  }
</style>
</head>
<body>

<section class="card card--loyalty">
  <div class="flourish" role="img" aria-label="Soft grey floral swirl decoration"></div>

  <div class="stylist">
    <p class="stylist__lead">your hair stylists</p>
    <p class="stylist__name">name is Tess</p>
  </div>

  <div class="punch">
    <div class="punch__slot"><div class="punch__box"></div><span class="punch__num">1</span></div>
    <div class="punch__slot"><div class="punch__box"></div><span class="punch__num">2</span></div>
    <div class="punch__slot"><div class="punch__box"></div><span class="punch__num">3</span></div>
  </div>
  <p class="offer">after every 2nd haircut<br>the third has <em>$5 off</em></p>

  <div class="appointment">
    <div class="appointment__head">your next appointment</div>
    <div class="appointment__row">
      <div class="appointment__icon">
        <svg width="14" height="14" viewBox="0 0 14 14"><rect x="1" y="2" width="12" height="11" fill="none" stroke="#fff" stroke-width="1.5"/><path d="M1 5.5h12M5 5.5v7.5M9 5.5v7.5M1 9h12" stroke="#fff" stroke-width="1"/></svg>
      </div>
      <div class="appointment__cell"></div><div class="appointment__cell"></div><div class="appointment__cell"></div>
    </div>
    <div class="appointment__row appointment__row--time">
      <div class="appointment__icon">
        <svg width="14" height="14" viewBox="0 0 14 14"><circle cx="7" cy="7" r="6" fill="#fff"/><path d="M7 3.5V7l2.5 1.5" stroke="#4a4a4a" stroke-width="1.4" fill="none"/></svg>
      </div>
      <div class="appointment__cell">pm<br>am</div><div class="appointment__cell">pm<br>am</div><div class="appointment__cell">pm<br>am</div>
    </div>
  </div>

  <div class="band">
    <div class="band__name"><b>Hair &amp; Beauty</b><span>@ Corrabin</span></div>
    <div class="band__rule"></div>
    <div class="social">
      <p class="social__lead">find us on Friendbook</p>
      <p class="social__page"><span class="social__mark"></span>Hair &amp; Beauty at Corrabin</p>
    </div>
  </div>
</section>

<section class="card card--contact">
  <div class="flourish" role="img" aria-label="Soft pink floral swirl decoration"></div>
  <div class="brand"><b>Hair &amp; Beauty</b><span>@ Corrabin</span></div>
  <div class="contact-band">
    <div class="contact-band__pill">
      <span class="contact-band__icon">
        <svg width="12" height="12" viewBox="0 0 12 12"><path d="M3 1l2 2.5-1.2 1.2a6 6 0 0 0 3.5 3.5L8.5 7 11 9l-1.2 1.8C5.5 11 1 6.5 1.2 2.2z" fill="#fff"/></svg>
      </span>
      <span class="contact-band__icon">
        <svg width="12" height="12" viewBox="0 0 12 12"><path d="M6 1.5 1 6h1.5v4.5h2.5V8h2v2.5h2.5V6H11z" fill="#fff"/></svg>
      </span>
    </div>
    <div class="contact-band__lines">
      <p>(07) 54 913 668</p>
      <p>Shop 2 3/9 Wollard st Corrabin Qld 4571</p>
    </div>
  </div>
</section>

</body>
</html>
```